Zielgruppe
Wir sind ein Restaurant und starten jetzt mit der Herstellung von eigenen Getränken wie z.B. Whisky, Gin, Rum, Weine, Liköre etc. Die erste Linie des Whiksy haben wir selbst entworfen möchten aber mehr Professionalität einbringen.
Aufgabenstellung
Beiliegend die beiden Flaschen welche bedruckt/beklebt werden (mit Flaschenbezeichnung) und unser LOGO als PSD.
Stichworte: Regional, Qualität, Beste Zutaten, keine Zusatzstoffe
Bezeichnungen: Silberfalter Whisky / Silberfalter Gin
Wichtig: Wiederkennungswert schaffen (Es sollen in Zukunft auch Weine, Liköre etc. produziert werden)
Infos Gin:
- 65 verschiedenen Botanicals
- Neben Blutorangen, Zitronen und Limetten, zeigt auch der Duft von Ingwer, Zitronengras und Kaffirlimettenblätter als Zitrusensemble das Facettenreichtum des Gins. Das Aromaspiel verändert sich nach etwas Zeit im Glas sehr deutlich. Dann zeigen sich starke Aromakomponenten wie Kardamom, Koriander oder Piment. Der Gin zeichnet sich aus durch seine Lebendigkeit
- 42%vol
- 500ml
Infos Whisky:
- 8 Jahre gereift
- Zur Vergärung unseres Whiskys verwenden wir eigens gezüchtete Frischhefe mit besonderen Fähigkeiten zur Bildung von sehr fruchtigen Gäraromen. Die Weichheit bekommt er durch die dreifache Destillation. Auch bei der Wahl unserer Gerste setzen wir auf unsere Region. Der Grund für diesen starken regionalen Bezug ist, dass wir versuchen unserem Whisky die größtmögliche Portion an Terroir zu verleihen. Bei der anschließenden Fasslagerung setzen wir auf hochwertige Fässer. Zuerst neue amerikanische Weißeiche mit anschließendem Sherry- und Cognacfass finish.
Tradition und Moderne verschmelzen zu einem unverwechselbaren Whisky, mit weichem, fruchtigen femininen Geschmack und wildem, maskulinen Charakter.
- Single Malt Whisky
- Geruch & Geschmack: Der Whisky zeichnet sich aus durch intensive, weiche Aromen nach Vanille und süßen Früchten, mit einem ungewöhnlich weichen und sanften Abgang mit einem Hauch von dunkler Schokolade.
Folgende obligatorischen Angaben sind Pflicht:
- Adresse 'Silberfalter / Lindenwiese 7 / 48213 Linkenheim-Hochstetten'
- Losnummer z.B. L0121..

```html
<!DOCTYPE html>
<html lang="en">
<head>
<meta charset="utf-8">
<title>Silberfalter Gin &amp; Whiskey</title>
<link rel="stylesheet" href="https://fonts.googleapis.com/css2?family=Great+Vibes&family=Cedarville+Cursive&family=Tinos&display=swap">
<style>
  :root {
    --backdrop: #e4e4e4;
    --glass: #1c1b19;
    --cap-gold: #c9a24a;
    --cap-rim: #a9832f;
    --gold: #d4a82a;
    --ink-white: #f2f0ea;
    --ink-grey: #9a9690;
  }
  * { margin: 0; padding: 0; box-sizing: border-box; }
  html, body { width: 1200px; height: 848px; overflow: hidden; background: var(--backdrop); }
  .canvas { position: relative; width: 1200px; height: 848px; }
  .bottle { position: absolute; top: 137px; width: 216px; height: 584px; }
  .bottle--gin { left: 321px; }
  .bottle--whiskey { left: 664px; }
  .bottle-shape { position: absolute; inset: 0; }
  .bottle-shape .glass { fill: var(--glass); }
  .bottle-shape .cap { fill: var(--cap-gold); }
  .bottle-shape .cap-rim { fill: var(--cap-rim); }
  .brand-ring {
    position: absolute; left: 75px; top: 236px; width: 66px; height: 66px;
    border: 1.5px solid var(--gold); border-radius: 50%;
  }
  .brand-name {
    position: absolute; left: 0; right: 0; top: 296px; text-align: center;
    font-family: "Great Vibes", cursive; font-size: 27px; color: var(--gold);
  }
  .product-name {
    position: absolute; left: 8px; right: 8px; top: 348px; height: 80px; text-align: center;
    font-family: "Great Vibes", cursive; line-height: 80px; color: var(--gold); white-space: nowrap;
  }
  .product-name--gin { font-size: 72px; }
  .product-name--whiskey { font-size: 54px; }
  .tasting-notes {
    position: absolute; left: 12px; right: 12px; top: 444px; text-align: center;
    transform: rotate(-2deg); transform-origin: center;
  }
  .tasting-notes p {
    font-family: "Cedarville Cursive", cursive; font-size: 8px; line-height: 13px;
    color: var(--ink-white); white-space: nowrap;
  }
  .volume {
    position: absolute; left: 0; right: 0; top: 530px; text-align: center;
    font-family: "Tinos", serif; font-size: 11px; color: var(--ink-grey);
  }
  .volume .divider { display: inline-block; width: 1px; height: 12px; background: var(--ink-grey); vertical-align: -2px; margin: 0 3px; }
  .legal {
    position: absolute; left: 8px; right: 8px; top: 549px; text-align: center;
    font-family: "Tinos", serif; font-size: 6.5px; line-height: 9px; color: var(--ink-grey); white-space: nowrap;
  }
</style>
</head>
<body>
<main class="canvas">

  <section class="bottle bottle--gin">
    <svg class="bottle-shape" viewBox="0 0 216 584" aria-hidden="true">
      <path class="glass" d="M67,44 L67,150 C67,166 0,160 0,192 L0,568 Q0,584 16,584 L200,584 Q216,584 216,568 L216,192 C216,160 149,166 149,150 L149,44 Z"/>
      <rect class="glass" x="62" y="36" width="92" height="12" rx="4"/>
      <rect class="cap" x="64" y="0" width="87" height="38" rx="4"/>
      <rect class="cap-rim" x="64" y="32" width="87" height="6"/>
    </svg>
    <div class="brand-ring"></div>
    <div class="brand-name">Silberfalter</div>
    <div class="product-name product-name--gin">Gin</div>
    <div class="tasting-notes">
      <p>- 65 different botanicals</p>
      <p>Besides blood oranges, lemons and limes, ginger,</p>
      <p>lemongrass and kaffir lime leaves show the</p>
      <p>many facets of this gin. With time in the glass</p>
      <p>cardamom, coriander and allspice appear.</p>
      <p>A gin marked by its liveliness.</p>
    </div>
    <div class="volume">42% vol<span class="divider"></span>500ml</div>
    <div class="legal">Silberfalter · Lindenwiese 7 · 48213 Linkenheim-Hochstetten<br>L0121</div>
  </section>

  <section class="bottle bottle--whiskey">
    <svg class="bottle-shape" viewBox="0 0 216 584" aria-hidden="true">
      <path class="glass" d="M67,44 L67,150 C67,166 0,160 0,192 L0,568 Q0,584 16,584 L200,584 Q216,584 216,568 L216,192 C216,160 149,166 149,150 L149,44 Z"/>
      <rect class="glass" x="62" y="36" width="92" height="12" rx="4"/>
      <rect class="cap" x="64" y="0" width="87" height="38" rx="4"/>
      <rect class="cap-rim" x="64" y="32" width="87" height="6"/>
    </svg>
    <div class="brand-ring"></div>
    <div class="brand-name">Silberfalter</div>
    <div class="product-name product-name--whiskey">Whiskey</div>
    <div class="tasting-notes">
      <p>- Single Malt, aged 8 years</p>
      <p>Fermented with our own fresh yeast for fruity</p>
      <p>aromas, softened by triple distillation. Our</p>
      <p>barley comes from the region for true terroir,</p>
      <p>aged in new American oak, finished in sherry</p>
      <p>and cognac casks. Vanilla, sweet fruit, chocolate.</p>
    </div>
    <div class="volume">42% vol<span class="divider"></span>500ml</div>
    <div class="legal">Silberfalter · Lindenwiese 7 · 48213 Linkenheim-Hochstetten<br>L0122</div>
  </section>

</main>
</body>
</html>
```